Bright Harbor Mortgage with a new LOGO needs new Business Card Design

We have a new logo from PixelForge and need to incorporate it into new business cards. All the cards will have to include: Logo, Co Name and Address, Photo of Loan Officer, personal NMLS # and company NMLS#, website address and phone,fax & cell number. I think I would like them vertical verses horizontal. I do not want a white background. Below is the information that is necessary on each card.
Continental Summit Mortgage #NMLS #4732 DBA (in very small letters)
Bright Harbor Mortgage Company
7142 NE Birchwood Lane, Suite 208
Lake Oswego, OR 97118
NMLS # 6391
p 503-xxx-xxxx
f 503-xxx-xxxx
c 503-xxx-xxxx
www.brightharbormortage-example.com
Then need
Photo of each LO with title of Mortgage Advisor
and NMLS# #xxxxx
Thanks.
Realtors, Loan Clients
Business

```html
<!DOCTYPE html>
<html lang="en">
<head>
<meta charset="utf-8">
<title>Bright Harbor Mortgage – Business Card</title>
<link href="https://fonts.googleapis.com/css2?family=Open+Sans:ital,wght@0,400;0,600;0,700;1,400;1,600&family=Arimo:wght@700&display=swap" rel="stylesheet">
<style>
  :root {
    --navy: #1a2640;
    --brand-blue: #263a94;
    --sky: #2597d4;
    --silver-light: #f1f1f2;
    --silver: #c9cacc;
    --silver-dark: #a9abae;
    --ink: #1d1d1f;
    --white: #ffffff;
  }
  * { margin: 0; padding: 0; box-sizing: border-box; }
  html, body { width: 1200px; height: 900px; overflow: hidden; background: var(--white); }
  body { position: relative; font-family: "Open Sans", Arial, sans-serif; color: var(--ink); }

  .card { position: absolute; width: 357px; height: 590px; overflow: hidden; }
  .card--front { left: 143px; top: 141px; }
  .card--back { left: 685px; top: 148px; width: 356px; }
  .card__bg { position: absolute; inset: 0; width: 100%; height: 100%; }

  .brand { position: absolute; text-align: center; color: var(--brand-blue); font-weight: 600; line-height: 1.05; }
  .brand__dot { display: block; margin: 0 auto; border-radius: 50%; background: var(--brand-blue); }
  .brand--front { left: 20px; width: 250px; top: 195px; }
  .brand--front .brand__dot { width: 46px; height: 46px; margin-bottom: 14px; }
  .brand--front .brand__name { font-size: 31px; letter-spacing: 0.5px; }
  .brand--front .brand__sub { font-size: 13px; letter-spacing: 4px; margin-top: 6px; padding-top: 5px; border-top: 1.5px solid var(--brand-blue); }

  .brand--back { left: 18px; width: 150px; top: 40px; }
  .brand--back .brand__dot { width: 26px; height: 26px; margin-bottom: 8px; }
  .brand--back .brand__name { font-size: 17px; }
  .brand--back .brand__sub { font-size: 7px; letter-spacing: 2px; margin-top: 3px; padding-top: 3px; border-top: 1px solid var(--brand-blue); }

  .advisor { position: absolute; left: 14px; width: 150px; top: 174px; text-align: right; color: var(--navy); }
  .advisor__name { font-size: 19px; line-height: 1.05; white-space: nowrap; letter-spacing: -0.2px; }
  .advisor__name strong { font-weight: 700; }
  .advisor__title { font-size: 12px; font-style: italic; font-weight: 600; }

  .portrait { position: absolute; left: 172px; top: 17px; width: 168px; height: 232px; border: 5px solid var(--sky); border-radius: 20px; overflow: hidden; background: var(--white); }
  .portrait__fill { width: 100%; height: 100%; border-radius: 15px; background: linear-gradient(180deg, #ececec 0%, #c8c8c8 45%, #26293a 75%, #1c1f2c 100%); }

  .contact { position: absolute; left: 23px; top: 300px; }
  .contact__address { font-size: 13px; font-weight: 600; line-height: 18px; }
  .contact__nmls { font-size: 12px; font-style: italic; line-height: 18px; }
  .contact__phones { margin-top: 14px; font-size: 17px; line-height: 21px; }
  .contact__phones strong { font-weight: 700; }
  .contact__web { margin-top: 16px; font-family: "Arimo", Arial, sans-serif; font-weight: 700; font-size: 11px; white-space: nowrap; }

  .disclosure { position: absolute; left: 335px; top: 560px; transform: rotate(-90deg); transform-origin: left top; white-space: nowrap; color: var(--white); font-family: "Arimo", Arial, sans-serif; font-weight: 700; font-size: 9.5px; }
</style>
</head>
<body>

<section class="card card--front" aria-label="Business card front">
  <svg class="card__bg" viewBox="0 0 357 590" preserveAspectRatio="none" aria-hidden="true">
    <defs>
      <radialGradient id="silverFront" cx="0.45" cy="0.5" r="0.75">
        <stop offset="0" stop-color="var(--silver-light)"/>
        <stop offset="0.6" stop-color="var(--silver)"/>
        <stop offset="1" stop-color="var(--silver-dark)"/>
      </radialGradient>
    </defs>
    <rect width="357" height="590" fill="url(#silverFront)"/>
    <path d="M226 0 C300 130 320 420 130 590 L357 590 L357 0 Z" fill="var(--sky)"/>
    <path d="M236 0 C312 130 332 420 152 590 L357 590 L357 0 Z" fill="var(--white)"/>
    <path d="M240 0 C330 130 345 420 180 590 L357 590 L357 0 Z" fill="var(--navy)"/>
  </svg>
  <div class="brand brand--front">
    <span class="brand__dot"></span>
    <div class="brand__name">Bright Harbor</div>
    <div class="brand__sub">MORTGAGE</div>
  </div>
</section>

<section class="card card--back" aria-label="Business card back">
  <svg class="card__bg" viewBox="0 0 356 590" preserveAspectRatio="none" aria-hidden="true">
    <defs>
      <radialGradient id="silverBack" cx="0.35" cy="0.5" r="0.8">
        <stop offset="0" stop-color="var(--silver-light)"/>
        <stop offset="0.6" stop-color="var(--silver)"/>
        <stop offset="1" stop-color="var(--silver-dark)"/>
      </radialGradient>
    </defs>
    <rect width="356" height="590" fill="url(#silverBack)"/>
    <path d="M228 0 C305 130 330 420 132 590 L356 590 L356 0 Z" fill="var(--sky)"/>
    <path d="M237 0 C316 130 340 420 152 590 L356 590 L356 0 Z" fill="var(--white)"/>
    <path d="M240 0 C330 130 350 420 185 590 L356 590 L356 0 Z" fill="var(--navy)"/>
  </svg>

  <div class="brand brand--back">
    <span class="brand__dot"></span>
    <div class="brand__name">Bright Harbor</div>
    <div class="brand__sub">MORTGAGE</div>
  </div>

  <div class="portrait">
    <div class="portrait__fill" role="img" aria-label="Portrait photo of the loan officer"></div>
  </div>

  <div class="advisor">
    <div class="advisor__name"><strong>DANIEL</strong> Reeves</div>
    <div class="advisor__title">Mortgage Advisor</div>
  </div>

  <div class="contact">
    <div class="contact__address">7142 NE Birchwood Lane<br>Suite 208<br>Lake Oswego, OR 97118</div>
    <div class="contact__nmls">NMLS # 6391</div>
    <div class="contact__phones">
      <div><strong>503-xxx-xxxx</strong>/phone</div>
      <div><strong>503-xxx-xxxx</strong>/fax</div>
      <div><strong>503-xxx-xxxx</strong>/cell</div>
    </div>
    <div class="contact__web">www.brightharbormortage-example.com</div>
  </div>

  <div class="disclosure">Continental Summit Mortgage #NMLS #4732 DBA</div>
</section>

</body>
</html>
```